Business Card - Harlow Birch

Need Business Card design for company named Harlow Birch. Software development focused mainly on Ardel eKallo & oBix Apps. I've attached our logo with both a black and white background. Please add trademark symbol to logo when using.

```html
<!DOCTYPE html>
<html lang="en">
<head>
<meta charset="utf-8">
<title>Harlow Birch – Business Card</title>
<link href="https://fonts.googleapis.com/css2?family=Open+Sans:wght@400;600;700&display=swap" rel="stylesheet">
<style>
  :root {
    --bg: #e9e6e1;
    --card-white: #ffffff;
    --card-black: #0b0b0b;
    --yellow: #f6c21a;
    --orange: #f39433;
    --red: #dc1f26;
    --grey: #7a7a7a;
    --ink: #1a1a1a;
  }
  * { margin: 0; padding: 0; box-sizing: border-box; }
  html, body { width: 1200px; height: 1014px; overflow: hidden; }
  body {
    background: var(--bg);
    font-family: "Open Sans", Arial, sans-serif;
    position: relative;
  }
  .card {
    position: absolute;
    width: 540px;
    height: 310px;
    background: var(--card-white);
    border-radius: 4px;
    overflow: hidden;
    box-shadow: 0 6px 18px rgba(0,0,0,0.18);
  }
  .card-front { left: 30px; top: 352px; }
  .card-back { left: 630px; top: 352px; }

  .front-band { position: absolute; left: 0; top: 0; width: 540px; height: 310px; }
  .contact {
    position: absolute;
    right: 34px;
    top: 20px;
    text-align right;
    text-align: right;
    color: #fff;
  }
  .contact .person { font-weight: 700; font-size: 21px; line-height: 1.15; }
  .contact .role { color: var(--red); font-weight: 700; font-size: 16px; line-height: 1.25; margin-bottom: 8px; }
  .contact .lines { font-size: 13px; line-height: 1.4; }

  .wordmark {
    position: absolute;
    display: flex;
    align-items: center;
    gap: 12px;
    color: var(--grey);
    font-weight: 600;
    white-space: nowrap;
  }
  .card-front .wordmark { left: 40px; bottom: 30px; font-size: 30px; }
  .wordmark .dot {
    width: 22px; height: 22px; border-radius: 50%;
    background: var(--orange);
    flex: none;
  }
  .wordmark sup { font-size: 11px; font-weight: 400; align-self: flex-start; margin-left: -8px; margin-top: 2px; }

  .card-back .wordmark { left: 50%; top: 110px; transform: translateX(-50%); font-size: 40px; }
  .card-back .wordmark .dot { width: 30px; height: 30px; background: var(--red); }
  .site {
    position: absolute;
    right: 34px;
    bottom: 28px;
    font-weight: 700;
    font-size: 18px;
    color: var(--ink);
  }
</style>
</head>
<body>
  <section class="card card-front" aria-label="Business card front">
    <svg class="front-band" viewBox="0 0 540 310" aria-hidden="true">
      <path d="M0 0 H540 V192 H300 C282 192 282 170 262 170 H210 C190 170 190 192 172 192 H0 Z" fill="var(--card-black)"/>
      <path d="M0 192 H172 C190 192 190 170 210 170 H262 C282 170 282 192 300 192 H540 V208 H300 C274 208 276 186 262 186 H210 C196 186 198 208 172 208 H0 Z" fill="var(--yellow)"/>
    </svg>
    <div class="contact">
      <p class="person">Elias Marwood</p>
      <p class="role">Manager</p>
      <p class="lines">555-214-6630 Mobile<br>elias@harlowbirch.com<br>4120 Linden Row<br>Fernvale, ST 40117<br>555-214-6631 Fax</p>
    </div>
    <div class="wordmark"><span class="dot"></span>Harlow Birch<sup>™</sup></div>
  </section>

  <section class="card card-back" aria-label="Business card back">
    <div class="wordmark"><span class="dot"></span>Harlow Birch</div>
    <p class="site">harlowbirch.com</p>
  </section>
</body>
</html>
```